Legal and business training card design

We need a business card design for POBAK - Pastoral Owners Bureau and Knowhow Agency a new company set up in county Victoria . Our aim is to assist regional business with their every day employment law legal issues and questions - this would include compliance within the workplace, employment conts, EBAs, dismissals, and general OHS. As well as POBAK will engage in training in particular Human Resources, management v leadership, time management , as well as constructing training around individual business/s needs. So we are multi purpose.
Our product is our service. It's designed specifically for regional base business hence we understand the requirements and needs of regional business v city business. At the same time the card must be simple, yet hard hitting, getting the message across in a couple of seconds.
I would like to see red and yellows, with perhaps a symbol/logo that represents the regional areas incorporated into the POBAK name ie curvy R in which the R's " right leg "expands under the entire acronym. Or you may have some better ideas. I also like the symbol of the square/s to match our slogan "Building workplace answers beyond the fence line".
Thanks
Industry/Entity Type
Training
Contact Information for Business Card
POBAK
Pastoral Owners Bureau & Knowhow Agency
"Building workplace answers beyond the fence line"
Fiona Brack B.A LL.B
Director and Principal
T: 1800 927 418 E: fiona@pobak.com.au
W: www.pobak.com.au

```html
<!DOCTYPE html>
<html lang="en">
<head>
<meta charset="utf-8">
<title>POBAK – Business Card</title>
<link rel="stylesheet" href="https://fonts.googleapis.com/css2?family=Didact+Gothic&family=Arimo:wght@400;700&display=swap">
<style>
  :root {
    --brand-red: #d8472a;
    --brand-yellow: #f4c233;
    --card-white: #ffffff;
    --page-bg: #ebe7e2;
    --shadow: rgba(0, 0, 0, 0.18);
  }
  * { box-sizing: border-box; margin: 0; padding: 0; }
  html, body {
    width: 1200px;
    height: 1000px;
    overflow: hidden;
    background: var(--page-bg);
  }
  .canvas {
    position: relative;
    width: 1200px;
    height: 1000px;
  }
  .card {
    position: absolute;
    width: 720px;
    height: 420px;
    background: var(--card-white);
    box-shadow: 0 6px 18px var(--shadow);
    overflow: hidden;
  }

  /* ---------- Front ---------- */
  .card--front { left: 70px; top: 60px; }
  .front__brand {
    position: absolute;
    top: 48px;
    left: 0;
    width: 100%;
    text-align: center;
  }
  .brand-name {
    font-family: "Didact Gothic", sans-serif;
    color: var(--brand-red);
    letter-spacing: 0.04em;
  }
  .front__brand .brand-name { font-size: 66px; line-height: 1; }
  .flourish {
    display: block;
    margin: 0 auto;
    background: linear-gradient(90deg, rgba(244,194,51,0), var(--brand-yellow) 30%, var(--brand-yellow) 70%, rgba(244,194,51,0));
    border-radius: 50%;
  }
  .front__brand .flourish { width: 110px; height: 16px; margin-top: 22px; }
  .front__title {
    position: absolute;
    top: 178px;
    left: 0;
    width: 100%;
    text-align: center;
    font-family: "Didact Gothic", sans-serif;
    color: var(--brand-red);
  }
  .front__title .title-main {
    font-size: 46px;
    font-weight: 700;
    letter-spacing: 0.02em;
    line-height: 1.05;
    -webkit-text-stroke: 1px var(--brand-red);
  }
  .front__title .title-sub {
    font-size: 22px;
    letter-spacing: 0.04em;
    margin-top: 4px;
  }
  .front__rule {
    position: absolute;
    left: 0;
    width: 100%;
    top: 312px;
    height: 4px;
    background: var(--brand-red);
  }
  .front__band {
    position: absolute;
    left: 0;
    width: 100%;
    top: 324px;
    bottom: 0;
    background: var(--brand-red);
    display: flex;
    align-items: flex-end;
    padding: 0 0 26px 44px;
  }
  .tagline {
    font-family: "Arimo", sans-serif;
    font-size: 23px;
    letter-spacing: 0.08em;
    color: var(--brand-yellow);
    white-space: nowrap;
  }

  /* ---------- Back ---------- */
  .card--back { left: 410px; top: 500px; }
  .back__head {
    position: absolute;
    top: 0;
    left: 0;
    width: 100%;
    height: 168px;
    text-align: center;
    padding-top: 30px;
  }
  .back__head .brand-name { font-size: 34px; line-height: 1; }
  .back__head .flourish { width: 70px; height: 9px; margin-top: 10px; }
  .back__title {
    font-family: "Arimo", sans-serif;
    color: var(--brand-red);
    margin-top: 8px;
  }
  .back__title .title-main { font-size: 20px; font-weight: 700; letter-spacing: 0.03em; }
  .back__title .title-sub { font-size: 11px; letter-spacing: 0.06em; margin-top: 2px; }
  .back__rule {
    position: absolute;
    left: 0;
    width: 100%;
    top: 170px;
    height: 3px;
    background: var(--brand-red);
  }
  .back__panel {
    position: absolute;
    left: 0;
    width: 100%;
    top: 180px;
    bottom: 0;
    background: var(--brand-red);
    text-align: center;
    font-family: "Arimo", sans-serif;
    color: var(--card-white);
    padding-top: 40px;
  }
  .contact-name { font-size: 23px; letter-spacing: 0.06em; line-height: 1.2; }
  .contact-name strong { font-weight: 700; }
  .contact-role {
    font-size: 17px;
    letter-spacing: 0.06em;
    color: var(--brand-yellow);
    margin-top: 6px;
  }
  .contact-list {
    list-style: none;
    margin-top: 30px;
    font-size: 20px;
    letter-spacing: 0.06em;
    line-height: 1.35;
  }
  .contact-list .label { color: var(--brand-yellow); }
</style>
</head>
<body>
<main class="canvas">

  <section class="card card--front" aria-label="Business card front">
    <div class="front__brand">
      <div class="brand-name">POBAK</div>
      <span class="flourish" role="img" aria-label="Small golden scroll ornament"></span>
    </div>
    <div class="front__title">
      <div class="title-main">PASTORAL OWNERS</div>
      <div class="title-sub">BUREAU &amp; KNOWHOW AGENCY</div>
    </div>
    <div class="front__rule"></div>
    <div class="front__band">
      <p class="tagline">Building workplace answers beyond the fence line</p>
    </div>
  </section>

  <section class="card card--back" aria-label="Business card back">
    <div class="back__head">
      <div class="brand-name">POBAK</div>
      <span class="flourish" role="img" aria-label="Small golden scroll ornament"></span>
      <div class="back__title">
        <div class="title-main">PASTORAL OWNERS</div>
        <div class="title-sub">BUREAU &amp; KNOWHOW AGENCY</div>
      </div>
    </div>
    <div class="back__rule"></div>
    <div class="back__panel">
      <p class="contact-name"><strong>Fiona Brack</strong> B.A LL.B</p>
      <p class="contact-role">Director and Principal</p>
      <ul class="contact-list">
        <li><span class="label">T:</span> 1800 927 418</li>
        <li><span class="label">E:</span> fiona@pobak.com.au</li>
        <li><span class="label">W:</span> www.pobak.com.au</li>
      </ul>
    </div>
  </section>

</main>
</body>
</html>
```